Criação de Papelaria Profissional para Consultoria de Negócios
" Somos uma empresa de consultoria para transportadoras, atuamos de forma operacional, fazemos um diagnóstico dos problemas da empresa, desenhamos processos, treinamos e auditamos o andamento, atuamos em todas os departamentos de uma transportadora. "

```html
<!DOCTYPE html>
<html lang="pt-BR">
<head>
<meta charset="UTF-8">
<title>Rota Consultoria – Papel Timbrado</title>
<link href="https://fonts.googleapis.com/css2?family=Exo+2:wght@400;700&display=swap" rel="stylesheet">
<style>
  :root {
    --brand-blue: #1f6fae;
    --brand-blue-dark: #1a5f96;
    --brand-orange: #e8792b;
    --paper: #ffffff;
    --backdrop: #e9eaec;
    --footer-text: #e6f0f8;
  }
  * { margin: 0; padding: 0; box-sizing: border-box; }
  html, body {
    width: 1200px;
    height: 1200px;
    overflow: hidden;
    background: var(--backdrop);
    font-family: "Exo 2", sans-serif;
  }
  .letterhead {
    position: absolute;
    left: 200px;
    top: 35px;
    width: 800px;
    height: 1130px;
    background: var(--paper);
  }
  .letterhead__header {
    position: absolute;
    left: 56px;
    right: 56px;
    top: 58px;
    display: flex;
    align-items: center;
    gap: 14px;
  }
  .brand-mark {
    width: 22px;
    height: 22px;
    background: var(--brand-orange);
    flex: none;
  }
  .brand-name {
    font-weight: 700;
    font-size: 30px;
    color: var(--brand-blue);
    letter-spacing: 0.3px;
    white-space: nowrap;
  }
  .header-rule {
    flex: 1;
    height: 2px;
    background: var(--brand-orange);
    margin-top: 14px;
  }
  .letterhead__footer {
    position: absolute;
    left: 0;
    right: 0;
    bottom: 42px;
    height: 40px;
    background: var(--brand-blue);
    border-top: 4px solid var(--brand-orange);
    display: flex;
    align-items: center;
    justify-content: space-around;
    padding: 0 20px;
  }
  .contact-item {
    display: flex;
    align-items: center;
    gap: 7px;
    font-size: 10.5px;
    color: var(--footer-text);
    white-space: nowrap;
  }
  .contact-icon {
    width: 16px;
    height: 16px;
    flex: none;
  }
</style>
</head>
<body>
  <main class="letterhead">
    <header class="letterhead__header">
      <span class="brand-mark" aria-hidden="true"></span>
      <span class="brand-name">Rota Consultoria</span>
      <span class="header-rule" aria-hidden="true"></span>
    </header>

    <footer class="letterhead__footer">
      <div class="contact-item">
        <svg class="contact-icon" viewBox="0 0 16 16" aria-hidden="true">
          <circle cx="8" cy="8" r="8" fill="#fff"/>
          <path d="M8 3.5a3 3 0 0 0-3 3c0 2.2 3 5.5 3 5.5s3-3.3 3-5.5a3 3 0 0 0-3-3z" fill="#1f6fae"/>
          <circle cx="8" cy="6.5" r="1.1" fill="#fff"/>
        </svg>
        <span>Av. Central, 1200 - Centro - Curitiba</span>
      </div>
      <div class="contact-item">
        <svg class="contact-icon" viewBox="0 0 16 16" aria-hidden="true">
          <circle cx="8" cy="8" r="8" fill="#fff"/>
          <path d="M5.4 4h1.6l.8 2-1 .8a5.5 5.5 0 0 0 2.4 2.4l.8-1 2 .8v1.6c0 .5-.4.9-.9.9A7.5 7.5 0 0 1 4.5 4.9c0-.5.4-.9.9-.9z" fill="#1f6fae"/>
        </svg>
        <span>(41) 3300-0000</span>
      </div>
      <div class="contact-item">
        <svg class="contact-icon" viewBox="0 0 16 16" aria-hidden="true">
          <circle cx="8" cy="8" r="8" fill="#fff"/>
          <path d="M8 3.5a3 3 0 0 0-3 3c0 2.2 3 5.5 3 5.5s3-3.3 3-5.5a3 3 0 0 0-3-3z" fill="#1f6fae"/>
          <circle cx="8" cy="6.5" r="1.1" fill="#fff"/>
        </svg>
        <span>Rua Alfa, 85 - Sala 4 - Londrina</span>
      </div>
      <div class="contact-item">
        <svg class="contact-icon" viewBox="0 0 16 16" aria-hidden="true">
          <circle cx="8" cy="8" r="8" fill="#fff"/>
          <path d="M5.4 4h1.6l.8 2-1 .8a5.5 5.5 0 0 0 2.4 2.4l.8-1 2 .8v1.6c0 .5-.4.9-.9.9A7.5 7.5 0 0 1 4.5 4.9c0-.5.4-.9.9-.9z" fill="#1f6fae"/>
        </svg>
        <span>(43) 3200-0000 / 3200-0001</span>
      </div>
    </footer>
  </main>
</body>
</html>
```